Corrow Family Farm fresh honey jar label

I need a label for jars of honey harvested at our farm. These are for gifts and personal use. We are looking to incorporate our farm brand into the label. We would like the design to take the existing brand and add some element like bees, honey, flowers, or hives to indicate the contents. We want the design to feel homemade and authentic without feeling cheap or hoaky

Requirements
Must have
• The label must be made to fit a 1" x2" rectangular label. The label must include the attached family brand. The label must include the text "Corrow Family Farms" "Pinebrook, USA" "Farm Fresh Honey". The label will be printed on off-white paper
Nice to have
• It would be nice to have illustrations of bees or flowers around the logo or hives or honeycombs. The label should have a vintage feel
Should not have
• The label should not feel overly cartoonish or hoaky

```html
<!DOCTYPE html>
<html lang="en">
<head>
<meta charset="UTF-8">
<title>Corrow Family Farms – Farm Fresh Honey Label</title>
<link href="https://fonts.googleapis.com/css2?family=Libre+Baskerville:wght@400;700&family=Montserrat:wght@500&display=swap" rel="stylesheet">
<style>
  :root {
    --backdrop: #f5f2ed;
    --paper: #f9f4ea;
    --ink: #1f1c18;
    --gold: #a9823e;
    --hive-tone: #cfc6b4;
    --hive-light: #ece5d6;
  }
  * { margin: 0; padding: 0; box-sizing: border-box; }
  html, body {
    width: 800px;
    height: 1200px;
    overflow: hidden;
    background: var(--backdrop);
  }
  .label {
    position: absolute;
    left: 140px;
    top: 82px;
    width: 523px;
    height: 1014px;
    background: var(--paper);
    border-radius: 34px;
    box-shadow: 0 2px 10px rgba(60, 45, 20, 0.08);
  }
  .brand-mark {
    position: absolute;
    left: 0;
    right: 0;
    top: 120px;
    display: flex;
    justify-content: center;
    align-items: center;
    gap: 14px;
    font-family: "Libre Baskerville", serif;
    font-weight: 700;
    font-size: 56px;
    letter-spacing: 4px;
    color: var(--ink);
  }
  .brand-mark .mark-square {
    width: 22px;
    height: 22px;
    background: var(--ink);
  }
  .farm-name {
    position: absolute;
    left: 0;
    right: 0;
    top: 315px;
    text-align: center;
    font-family: "Libre Baskerville", serif;
    font-weight: 700;
    font-size: 33px;
    line-height: 55px;
    color: var(--ink);
  }
  .farm-location {
    position: absolute;
    left: 0;
    right: 0;
    top: 436px;
    text-align: center;
    font-family: "Montserrat", sans-serif;
    font-weight: 500;
    font-size: 21px;
    letter-spacing: 1.5px;
    color: var(--ink);
  }
  .divider {
    position: absolute;
    display: block;
  }
  .divider-top { left: 120px; top: 482px; }
  .divider-bottom { left: 32px; top: 905px; }
  .product-kicker {
    position: absolute;
    left: 0;
    right: 0;
    top: 522px;
    text-align: center;
    font-family: "Libre Baskerville", serif;
    font-weight: 700;
    font-size: 27px;
    letter-spacing: 2.5px;
    color: var(--gold);
  }
  .product-name {
    position: absolute;
    left: 0;
    right: 0;
    top: 558px;
    text-align: center;
    font-family: "Libre Baskerville", serif;
    font-weight: 400;
    font-size: 64px;
    letter-spacing: 3px;
    color: var(--gold);
  }
  .hive-illustration {
    position: absolute;
    left: 46px;
    top: 648px;
    width: 420px;
    height: 196px;
    border-radius: 90px 90px 6px 6px;
    background: radial-gradient(ellipse at 50% 40%, var(--hive-light) 0%, var(--hive-tone) 75%);
  }
</style>
</head>
<body>
  <main class="label">
    <div class="brand-mark"><span class="mark-square"></span>CORROW</div>

    <h1 class="farm-name">CORROW<br>FAMILY FARMS</h1>
    <p class="farm-location">PINEBROOK, USA</p>

    <svg class="divider divider-top" width="280" height="12" viewBox="0 0 280 12" aria-hidden="true">
      <line x1="0" y1="6" x2="128" y2="6" stroke="var(--ink)" stroke-width="1.4"/>
      <circle cx="140" cy="6" r="4.5" fill="var(--ink)"/>
      <line x1="152" y1="6" x2="280" y2="6" stroke="var(--ink)" stroke-width="1.4"/>
    </svg>

    <h2 class="product-kicker">FARM FRESH</h2>
    <h2 class="product-name">HONEY</h2>

    <div class="hive-illustration" role="img" aria-label="Engraved illustration of a woven straw beehive on a wooden stand flanked by flowering sprigs"></div>

    <svg class="divider divider-bottom" width="459" height="12" viewBox="0 0 459 12" aria-hidden="true">
      <line x1="0" y1="5" x2="459" y2="5" stroke="var(--ink)" stroke-width="1.4"/>
      <line x1="30" y1="8" x2="429" y2="8" stroke="var(--ink)" stroke-width="0.7"/>
    </svg>
  </main>
</body>
</html>
```